Im open to ideas.. I was thinking on my business cards aswell as my logo. a place for my name. email. phone number and abn..

ive attched a file with my business logo. which i dont love the colours.. i was think a dark background with charcoal letters so something along those colour schumes but im open to ideas..

Industry/Entity Type

Business

Logo Text

RLB Constructions

```html
<!DOCTYPE html>
<html lang="en">
<head>
<meta charset="utf-8">
<title>RLB Constructions – Business Card</title>
<link rel="stylesheet" href="https://fonts.googleapis.com/css2?family=Michroma&display=swap">
<style>
  :root {
    --backdrop: #8c8c8c;
    --card: #3d3d3d;
    --ink: #ffffff;
  }
  * { margin: 0; padding: 0; box-sizing: border-box; }
  html, body {
    width: 1200px;
    height: 852px;
    overflow: hidden;
    background: var(--backdrop);
  }
  .canvas {
    position: relative;
    width: 1200px;
    height: 852px;
  }
  .business-card {
    position: absolute;
    left: 232px;
    top: 187px;
    width: 758px;
    height: 463px;
    border-radius: 20px;
    background: var(--card);
    font-family: "Michroma", sans-serif;
    color: var(--ink);
  }
  .brand-name {
    position: absolute;
    left: 0;
    right: 0;
    top: 142px;
    text-align: center;
    font-size: 40px;
    letter-spacing: 2px;
    text-transform: uppercase;
    color: var(--ink);
  }
  .holder-name {
    position: absolute;
    left: 43px;
    top: 390px;
    font-size: 22px;
    text-transform: uppercase;
  }
  .contact-list {
    position: absolute;
    right: 34px;
    top: 314px;
    list-style: none;
    display: flex;
    flex-direction: column;
    align-items: flex-end;
    gap: 18px;
  }
  .contact-item {
    display: flex;
    align-items: center;
    gap: 14px;
    font-size: 14.5px;
    line-height: 24px;
    text-transform: uppercase;
    letter-spacing: 0.5px;
  }
  .contact-item--abn { margin-right: 46px; }
  .contact-icon {
    width: 32px;
    height: 32px;
    flex: none;
  }
</style>
</head>
<body>
<main class="canvas">
  <section class="business-card" aria-label="RLB Constructions business card">
    <h1 class="brand-name">RLB Constructions</h1>

    <p class="holder-name">Your Name</p>

    <ul class="contact-list">
      <li class="contact-item contact-item--abn">ABN 12 345 678 910</li>
      <li class="contact-item">
        <span>0400 000 000</span>
        <svg class="contact-icon" viewBox="0 0 32 32" aria-hidden="true">
          <rect x="9" y="1.5" width="14" height="29" rx="2.5" fill="none" stroke="#fff" stroke-width="1.8"/>
          <line x1="9" y1="6" x2="23" y2="6" stroke="#fff" stroke-width="1.4"/>
          <line x1="9" y1="25" x2="23" y2="25" stroke="#fff" stroke-width="1.4"/>
        </svg>
      </li>
      <li class="contact-item">
        <span>email@email.com.au</span>
        <svg class="contact-icon" viewBox="0 0 32 32" aria-hidden="true">
          <rect x="0" y="6" width="32" height="20" fill="#fff"/>
          <polyline points="0,7 16,18 32,7" fill="none" stroke="#3d3d3d" stroke-width="1.8"/>
        </svg>
      </li>
    </ul>
  </section>
</main>
</body>
</html>
```